UI Mockup For Online Scheduling Software

11.01.2018 - Brief Update:
The brief has not changed but the summary below as being added to aid designers.

- New file added "Updated 11.01.2018 - Individual Box" to clarify the sections. Specifically the primary tag section
- Improve on the current styling
- Consider changing the section layout to maximise the number of blocks displayed on screen (The sections dont not need to be stacked like the current version.
- The design is for the application running on a desktop PC with 16:9 screen aspect
- The design styling/layout should not look like the current version
- You may use the application to get an understanding of its workings at this link....https://marlowtesk.brivanlabs.com.au/
- Think outside the box....use your creative flare and show me something different to the current app (style and layout)

There are already some good submissions so closer to the deadline I will increase the budget and award $$$ to 1st and 2nd. The winner will be chosen to directly work on the remaining aspects of this application (setting page, mobile design, dashboard etc). The next design project associated to this application will be 10 time bigger than this one.

Good Luck Designers

*************************************************************
Redesign the user interface to make more efficient use of the screen real estate.

The software works by adding (Drag & Drop) Project Blocks to a Date Section. Then tags are added (Drag & Drop) to the block section below the header, and then resources are added to the block section below the tags.
Each block has 4 main sections that are stacked vertically:

1. Header - Displays Title and Address
2. Tags - Displays tags, maximum of 6 tags
3. Resources - Displays resources, maximum of 10 resources, NOTE: this section can be hidded.
4. Footer - Display basic stats (eg. 3 Resources assigned)

It is critical that as many block (20-30) as possible for a single date can be visible on screen.

The following criteria must be considered when mocking up layout:
1. Font Type, size, colour and emphasis
2. Block Colour/Shading, borders ect
3. Section Layout within the block (stacking & Alignment)
4. Mock ups to show scaled layout of blocks in both the open state and Closed State.
5. Mock up to display a minimum of 20 blocks.
6. Create a variation of your design that adds a 5th section. This will display the first tag only:
1. Header - Always Visible
2. Primary Tag - Always Visible
3. Secondary Tags - Can be hidden
4. Resources - Can be Hidden
5. Footer - Can be Hidden

Please be creative with your design and layout. I like a clean, minimalist design.
At this stage CSS file will not be required but would be benificial
Updates

Designs look the same

Target Market(s)

N/A

Industry/Entity Type

Software

Number of Pages Required

1 page

Font styles to use
Other font styles liked:
• Designers Choice

Colors

Designer to choose colors to be used in the design.

Requirements
Must have
• Variation to current layout and style
Should not have
• Same styling and layout as current design

```html
<!DOCTYPE html>
<html lang="en">
<head>
<meta charset="utf-8">
<title>Gunite Pacific – Resources</title>
<link rel="stylesheet" href="https://fonts.googleapis.com/css2?family=Lato:wght@400;700;900&display=swap">
<style>
:root{
  --navy:#1e3b57;
  --navy-deep:#142c44;
  --rail:#1f2733;
  --rail-icon:#8a96a6;
  --accent:#1f86d6;
  --accent-dark:#1466b0;
  --ink:#27323f;
  --ink-soft:#6c7785;
  --ink-faint:#9aa4b1;
  --line:#e4e8ee;
  --panel:#ffffff;
  --board:#eef1f5;
  --pill:#f2f4f7;
  --orange:#f29b1d;
  --purple:#a05ad6;
  --red:#e23b4a;
  --green:#22b44d;
  --blue-tint:#e6f2fb;
  --yellow-tint:#fdf7dc;
  --green-tint:#e3f7ea;
  --yellow:#f5c518;
}
*{box-sizing:border-box;margin:0;padding:0}
html,body{width:1200px;height:979px;overflow:hidden}
body{font-family:"Lato",sans-serif;color:var(--ink);background:var(--board)}
svg.ic{width:12px;height:12px;fill:currentColor;flex:none}

.app{display:grid;grid-template-columns:48px 190px 1fr;grid-template-rows:50px 1fr;width:1200px;height:979px}

/* top bar */
.topbar{grid-column:1/-1;background:var(--navy);display:flex;align-items:center;padding:0 18px 0 14px;color:#fff;position:relative}
.menu{width:18px;height:14px;display:flex;flex-direction:column;justify-content:space-between;margin-right:16px}
.menu span{height:2px;background:#fff;border-radius:1px}
.brand{font-weight:700;font-size:15px;color:#7cc3f2;letter-spacing:-.2px}
.brand b{color:#fff;font-weight:700}
.date-nav{position:absolute;left:50%;transform:translateX(-50%);background:var(--navy-deep);border-radius:16px;height:30px;width:262px;display:flex;align-items:center;justify-content:space-between;padding:0 12px;font-weight:700;font-size:14px}
.date-nav svg{width:10px;height:12px;stroke:#fff;fill:none;stroke-width:2}
.greet{margin-left:auto;font-style:italic;font-size:14px;font-weight:700;display:flex;align-items:center;gap:10px}
.avatar{width:28px;height:28px;border-radius:50%;background:linear-gradient(135deg,#d99a78,#7a4b3a);border:2px solid #fff}
.greet .caret{width:8px;height:6px;stroke:#fff;fill:none;stroke-width:1.6}

/* rail */
.rail{background:var(--rail);display:flex;flex-direction:column;align-items:center;padding-top:14px;gap:22px;color:var(--rail-icon)}
.rail svg{width:20px;height:20px;fill:currentColor}
.rail .on{color:#5db3ee}
.rail .bottom{margin-top:auto;margin-bottom:14px}

/* resources panel */
.res{background:#fff;border-right:1px solid var(--line);overflow:hidden}
.res-tabs{display:flex;align-items:center;justify-content:space-around;padding:12px 10px 4px;color:#8b97a6}
.res-tabs svg{width:15px;height:15px;fill:currentColor}
.res-tabs .on{width:28px;height:28px;border-radius:50%;background:var(--navy);color:#fff;display:grid;place-items:center}
.res-head{display:flex;justify-content:space-between;align-items:center;padding:6px 12px 6px 11px}
.res-head h2{font-size:17px;font-weight:700;color:var(--navy)}
.count{background:var(--navy);color:#fff;font-size:9px;font-weight:700;width:19px;height:19px;border-radius:50%;display:grid;place-items:center}
.search{display:flex;align-items:center;gap:9px;background:#f1f3f6;padding:7px 12px;font-size:11px;color:var(--ink)}
.group{padding:0 22px 0 12px}
.group h3{display:flex;justify-content:space-between;font-size:11px;font-weight:700;color:var(--navy);padding:14px 0 6px}
.group h3 svg{width:8px;height:6px;stroke:var(--navy);fill:none;stroke-width:1.8}
.member{display:flex;align-items:center;gap:6px;background:#f1f3f6;height:24px;margin-bottom:4px;padding:0 8px;font-size:11px;color:var(--ink)}
.member svg{color:#7d8997;width:11px;height:11px}
.member .add{margin-left:auto;color:var(--ink-faint);font-size:13px}

/* board */
.board{overflow:hidden;padding:0 18px}
.toolbar{display:flex;align-items:center;height:56px;font-size:13px;color:var(--ink)}
.toggle{width:36px;height:20px;border-radius:10px;background:#e4e8ee;margin-left:12px;position:relative}
.toggle::after{content:"";position:absolute;right:0;top:-1px;width:22px;height:22px;border-radius:50%;background:linear-gradient(135deg,var(--accent),var(--accent-dark))}
.stat{display:flex;align-items:center;gap:8px;margin-left:auto}
.stat strong{color:var(--navy);font-weight:700}
.bar{width:62px;height:7px;border-radius:4px;background:#dfe4ea;overflow:hidden}
.bar i{display:block;height:100%;background:linear-gradient(90deg,var(--accent),var(--accent-dark));border-radius:4px}
.stat+.stat{margin-left:62px}
.filter{margin-left:62px;background:#fff;border-radius:3px;padding:7px 14px;display:flex;gap:10px;align-items:center;font-size:13px;box-shadow:0 1px 2px rgba(0,0,0,.05)}
.filter svg{width:15px;height:12px;fill:#7b8796}
.legend{display:flex;justify-content:space-between;padding:0 60px 0 44px;font-size:11px;height:24px;align-items:center;margin-bottom:10px}
.legend span{display:flex;align-items:center;gap:10px}
.legend svg{width:11px;height:11px}
.dot{width:9px;height:9px;border-radius:50%;display:inline-block;flex:none}
.d-orange{background:var(--orange)}.d-purple{background:var(--purple)}.d-red{background:var(--red)}.d-green{background:var(--green)}

.cols{display:grid;grid-template-columns:repeat(4,1fr);gap:17px}
.col{display:flex;flex-direction:column;gap:17px}

/* project block */
.block{background:var(--panel);border-radius:3px;box-shadow:0 1px 3px rgba(20,40,70,.08);padding:8px 9px 7px}
.block-head{display:flex;justify-content:space-between;align-items:flex-start}
.block-head h4{font-size:11px;font-weight:700;color:var(--ink)}
.block-head p{font-size:8px;color:var(--ink-soft);margin-top:2px}
.block-head svg{width:13px;height:13px;fill:#5f6b79}
.primary{display:flex;align-items:center;gap:8px;height:20px;padding:0 9px;margin:8px 0 10px;font-size:9px;border-radius:2px}
.primary svg{width:9px;height:9px}
.primary .x{margin-left:auto;color:var(--ink-faint)}
.p-blue{background:var(--blue-tint)}.p-blue svg{fill:var(--accent)}
.p-yellow{background:var(--yellow-tint)}.p-yellow svg{fill:var(--yellow)}
.p-green{background:var(--green-tint)}.p-green svg{fill:var(--green)}
.split{display:grid;grid-template-columns:1fr 1fr;gap:8px}
.label{font-size:6.5px;letter-spacing:.3px;color:var(--ink-soft);margin-bottom:5px}
.pill{display:flex;align-items:center;gap:6px;background:var(--pill);height:19px;padding:0 7px;margin-bottom:4px;font-size:8.5px;color:var(--ink)}
.pill .dot{width:7px;height:7px}
.pill svg{width:8px;height:8px;color:var(--navy)}
.pill .x{margin-left:auto;color:var(--ink-faint);font-size:9px}
.pill.ok{color:var(--green)}
.drop{border:1px dashed #b6c4d6;height:19px;display:grid;place-items:center;font-size:6.5px;color:#7d90a8;margin-bottom:4px}
.foot{display:flex;justify-content:space-between;align-items:center;margin-top:6px;color:#7b8796}
.foot svg{width:12px;height:12px}
.foot .who,.foot .talk{position:relative}
.foot b{position:absolute;top:-5px;right:-5px;background:var(--red);color:#fff;font-size:5.5px;font-weight:700;width:8px;height:8px;border-radius:50%;display:grid;place-items:center}
.foot .talk{margin-left:auto;margin-right:auto}
</style>
</head>
<body>
<svg width="0" height="0" style="position:absolute" aria-hidden="true">
  <symbol id="i-user" viewBox="0 0 16 16"><circle cx="8" cy="8" r="8" fill="currentColor"/><circle cx="8" cy="6" r="2.6" fill="#fff"/><path d="M3.5 12.6c1-2 2.6-2.8 4.5-2.8s3.5.8 4.5 2.8" fill="#fff"/></symbol>
  <symbol id="i-tag" viewBox="0 0 16 16"><path d="M1 1h7l7 7-7 7-7-7z M4.5 3.2a1.3 1.3 0 1 0 0 2.6 1.3 1.3 0 0 0 0-2.6z"/></symbol>
  <symbol id="i-gear" viewBox="0 0 16 16"><path d="M7 0h2l.4 2.1 1.5.6 1.8-1.2 1.4 1.4-1.2 1.8.6 1.5L16 7v2l-2.1.4-.6 1.5 1.2 1.8-1.4 1.4-1.8-1.2-1.5.6L9 16H7l-.4-2.1-1.5-.6-1.8 1.2-1.4-1.4 1.2-1.8-.6-1.5L0 9V7l2.1-.4.6-1.5-1.2-1.8 1.4-1.4 1.8 1.2 1.5-.6zM8 5a3 3 0 1 0 0 6 3 3 0 0 0 0-6z"/></symbol>
  <symbol id="i-chat" viewBox="0 0 16 16"><path d="M1 2h10v7H5l-3 2.5V9H1z" fill="currentColor"/><path d="M12 5h3v7h-1v2l-2.5-2H7v-2h5z" fill="currentColor" opacity=".7"/></symbol>
  <symbol id="i-chart" viewBox="0 0 16 16"><path d="M1 15h14v1H1zM3 9h2v5H3zM7 5h2v9H7zM11 7h2v7h-2z" fill="currentColor"/></symbol>
  <symbol id="i-people" viewBox="0 0 20 16"><circle cx="10" cy="5" r="3"/><circle cx="4" cy="6" r="2.2"/><circle cx="16" cy="6" r="2.2"/><path d="M4.5 14c0-3 2.5-5 5.5-5s5.5 2 5.5 5zM0 13c0-2 1.5-3.5 4-3.5l-.7 3.5zM20 13c0-2-1.5-3.5-4-3.5l.7 3.5z"/></symbol>
  <symbol id="i-folder" viewBox="0 0 20 16"><path d="M0 2h7l2 2h11v12H0z"/></symbol>
  <symbol id="i-building" viewBox="0 0 20 20"><path d="M2 19V8l5-3v3l5-3v3l5-3v14zM5 11h2v2H5zm4 0h2v2H9zm4 0h2v2h-2zM5 15h2v2H5zm4 0h2v2H9zm4 0h2v2h-2z"/></symbol>
  <symbol id="i-gauge" viewBox="0 0 20 20"><circle cx="10" cy="10" r="8.5" fill="none" stroke="currentColor" stroke-width="2"/><path d="M10 11l5-5-1 1z" stroke="currentColor" stroke-width="2"/><path d="M4 13h12v2H4z"/></symbol>
  <symbol id="i-worker" viewBox="0 0 20 20"><path d="M5 7a5 5 0 0 1 10 0zM3 7h14v1.5H3zM6.5 9.5h7a3.5 3.5 0 0 1-7 0zM2 20c0-4 3.5-6 8-6s8 2 8 6z"/></symbol>
  <symbol id="i-search" viewBox="0 0 16 16"><circle cx="6.5" cy="6.5" r="5" fill="none" stroke="currentColor" stroke-width="1.8"/><path d="M10 10l5 5" stroke="currentColor" stroke-width="1.8"/></symbol>
</svg>

<div class="app">
  <header class="topbar">
    <div class="menu"><span></span><span></span><span></span></div>
    <div class="brand"><b>Gunite</b>Pacific</div>
    <div class="date-nav">
      <svg viewBox="0 0 10 12"><path d="M8 1L3 6l5 5"/></svg>
      <span>Wednesday, Jan 10</span>
      <svg viewBox="0 0 10 12"><path d="M2 1l5 5-5 5"/></svg>
    </div>
    <div class="greet">Good day, Lester!
      <span class="avatar" role="img" aria-label="User profile photo"></span>
      <svg class="caret" viewBox="0 0 8 6"><path d="M1 1l3 3 3-3"/></svg>
    </div>
  </header>

  <nav class="rail">
    <svg class="on"><use href="#i-gauge"/></svg>
    <svg viewBox="0 0 20 16"><use href="#i-folder"/></svg>
    <svg><use href="#i-user"/></svg>
    <svg viewBox="0 0 20 20"><use href="#i-building"/></svg>
    <svg><use href="#i-tag"/></svg>
    <svg viewBox="0 0 20 20"><use href="#i-worker"/></svg>
    <svg class="bottom"><use href="#i-gear"/></svg>
  </nav>

  <aside class="res">
    <div class="res-tabs">
      <svg viewBox="0 0 20 16"><use href="#i-folder"/></svg>
      <span class="on"><svg viewBox="0 0 20 16"><use href="#i-people"/></svg></span>
      <svg viewBox="0 0 20 20"><use href="#i-building"/></svg>
      <svg><use href="#i-tag"/></svg>
    </div>
    <div class="res-head"><h2>Resources</h2><span class="count">67</span></div>
    <div class="search"><svg class="ic" viewBox="0 0 16 16"><use href="#i-search"/></svg>Search</div>

    <div class="group"><h3>1.0 JIGGERS<svg viewBox="0 0 8 6"><path d="M1 5l3-3 3 3"/></svg></h3>
      <div class="member"><svg><use href="#i-user"/></svg>Allan P.<span class="add">+</span></div>
      <div class="member"><svg><use href="#i-user"/></svg>Joseph S.<span class="add">+</span></div>
    </div>
    <div class="group"><h3>2.0 DOORS<svg viewBox="0 0 8 6"><path d="M1 5l3-3 3 3"/></svg></h3>
      <div class="member"><svg><use href="#i-user"/></svg>Christopher D.<span class="add">+</span></div>
      <div class="member"><svg><use href="#i-user"/></svg>Harrison J.<span class="add">+</span></div>
      <div class="member"><svg><use href="#i-user"/></svg>Maynard L.<span class="add">+</span></div>
    </div>
    <div class="group"><h3>3.0 CORNERS<svg viewBox="0 0 8 6"><path d="M1 5l3-3 3 3"/></svg></h3>
      <div class="member"><svg><use href="#i-user"/></svg>Dennis M.<span class="add">+</span></div>
      <div class="member"><svg><use href="#i-user"/></svg>Elnathan R.<span class="add">+</span></div>
      <div class="member"><svg><use href="#i-user"/></svg>Nicholas E.<span class="add">+</span></div>
    </div>
    <div class="group"><h3>4.0 SHELVING<svg viewBox="0 0 8 6"><path d="M1 5l3-3 3 3"/></svg></h3>
      <div class="member"><svg><use href="#i-user"/></svg>Ferdnando C.<span class="add">+</span></div>
      <div class="member"><svg><use href="#i-user"/></svg>Richard T.<span class="add">+</span></div>
    </div>
    <div class="group"><h3>5.0 ROAD CREW<svg viewBox="0 0 8 6"><path d="M1 5l3-3 3 3"/></svg></h3>
      <div class="member"><svg><use href="#i-user"/></svg>Alexander G.<span class="add">+</span></div>
      <div class="member"><svg><use href="#i-user"/></svg>Charlie J.<span class="add">+</span></div>
      <div class="member"><svg><use href="#i-user"/></svg>Ephraim H.<span class="add">+</span></div>
      <div class="member"><svg><use href="#i-user"/></svg>Harvey F.<span class="add">+</span></div>
      <div class="member"><svg><use href="#i-user"/></svg>Zachary E.<span class="add">+</span></div>
    </div>
  </aside>

  <main class="board">
    <div class="toolbar">
      <span>Show More Details</span><span class="toggle"></span>
      <span class="stat">Projects Assigned <strong>40 of 54</strong><span class="bar"><i style="width:82%"></i></span></span>
      <span class="stat">Resources Scheduled <strong>38 of 67</strong><span class="bar"><i style="width:60%"></i></span></span>
      <span class="filter"><svg viewBox="0 0 15 12"><path d="M0 0h10L6 5v5L4 12V5zM11 4h4v1.5h-4zM11 7h4v1.5h-4zM11 10h4v1.5h-4z"/></svg>Filter</span>
    </div>
    <div class="legend">
      <span><svg style="color:var(--navy)"><use href="#i-user"/></svg>Supervisor</span>
      <span><svg style="color:#8a96a6"><use href="#i-user"/></svg>Workers</span>
      <span><svg style="fill:var(--accent)"><use href="#i-tag"/></svg>Trades</span>
      <span><i class="dot d-orange"></i>Task</span>
      <span><i class="dot d-purple"></i>Notes</span>
      <span><i class="dot d-red"></i>Starts</span>
      <span><i class="dot d-green"></i>Status</span>
    </div>

    <div class="cols">
      <!-- column 1 -->
      <div class="col">
        <article class="block">
          <div class="block-head"><div><h4>CAG de Oro Heritage</h4><p>The Golden Friendship St, CDO City</p></div><svg><use href="#i-gear"/></svg></div>
          <div class="primary p-blue"><svg><use href="#i-tag"/></svg>Shotcrete<span class="x">×</span></div>
          <div class="split">
            <div><div class="label">PROJECT TAGS</div>
              <div class="pill"><i class="dot d-orange"></i>Kellmor<span class="x">×</span></div>
              <div class="pill"><i class="dot d-red"></i>7:30 am<span class="x">×</span></div>
              <div class="drop">Drag &amp; Drop Tags</div></div>
            <div><div class="label">RESOURCES</div>
              <div class="pill"><svg><use href="#i-user"/></svg>Elnathan R.<span class="x">×</span></div>
              <div class="drop">Drag &amp; Drop Resources</div></div>
          </div>
          <div class="foot"><span class="who"><svg><use href="#i-user"/></svg><b>1</b></span><span class="talk"><svg><use href="#i-chat"/></svg></span><svg><use href="#i-chart"/></svg></div>
        </article>
        <article class="block">
          <div class="block-head"><div><h4>Gran Europa</h4><p>Mastersons Avenue, Airport Road, CDO</p></div><svg><use href="#i-gear"/></svg></div>
          <div class="primary p-green"><svg><use href="#i-tag"/></svg>Anchoring<span class="x">×</span></div>
          <div class="split">
            <div><div class="label">PROJECT TAGS</div>
              <div class="pill"><i class="dot d-orange"></i>Dril &amp; Install<span class="x">×</span></div>
              <div class="pill"><i class="dot d-purple"></i>Night Shift<span class="x">×</span></div>
              <div class="pill"><i class="dot d-red"></i>8:00 pm<span class="x">×</span></div>
              <div class="pill ok"><i class="dot d-green"></i>Confirmed<span class="x">×</span></div>
              <div class="drop">Drag &amp; Drop Tags</div></div>
            <div><div class="label">RESOURCES</div>
              <div class="pill"><svg><use href="#i-user"/></svg>Christoher D.<span class="x">×</span></div>
              <div class="pill"><svg style="color:#8a96a6"><use href="#i-user"/></svg>Ephraim H.<span class="x">×</span></div>
              <div class="pill"><svg style="color:#8a96a6"><use href="#i-user"/></svg>Harvey F.<span class="x">×</span></div>
              <div class="drop">Drag &amp; Drop Resources</div></div>
          </div>
          <div class="foot"><span class="who"><svg><use href="#i-user"/></svg><b>3</b></span><span class="talk"><svg><use href="#i-chat"/></svg></span><svg><use href="#i-chart"/></svg></div>
        </article>
        <article class="block">
          <div class="block-head"><div><h4>CAG de Oro Heritage</h4><p>The Golden Friendship St, CDO City</p></div><svg><use href="#i-gear"/></svg></div>
          <div class="primary p-blue"><svg><use href="#i-tag"/></svg>Shotcrete<span class="x">×</span></div>
          <div class="split">
            <div><div class="label">PROJECT TAGS</div>
              <div class="pill"><i class="dot d-orange"></i>Kellmor<span class="x">×</span></div>
              <div class="pill"><i class="dot d-red"></i>7:30 am<span class="x">×</span></div>
              <div class="drop">Drag &amp; Drop Tags</div></div>
            <div><div class="label">RESOURCES</div>
              <div class="pill"><svg><use href="#i-user"/></svg>Elnathan R.<span class="x">×</span></div>
              <div class="drop">Drag &amp; Drop Resources</div></div>
          </div>
          <div class="foot"><span class="who"><svg><use href="#i-user"/></svg><b>1</b></span><span class="talk"><svg><use href="#i-chat"/></svg></span><svg><use href="#i-chart"/></svg></div>
        </article>
      </div>

      <!-- column 2 -->
      <div class="col">
        <article class="block">
          <div class="block-head"><div><h4>ABC Oroquieta</h4><p>Poblacion 1, Town Center, Oroquieta City</p></div><svg><use href="#i-gear"/></svg></div>
          <div class="primary p-yellow"><svg><use href="#i-tag"/></svg>Steel<span class="x">×</span></div>
          <div class="split">
            <div><div class="label">PROJECT TAGS</div>
              <div class="pill"><i class="dot d-orange"></i>Barrow<span class="x">×</span></div>
              <div class="pill"><i class="dot d-red"></i>4:00 pm<span class="x">×</span></div>
              <div class="pill ok"><i class="dot d-green"></i>Confirmed<span class="x">×</span></div>
              <div class="drop">Drag &amp; Drop Tags</div></div>
            <div><div class="label">RESOURCES</div>
              <div class="pill"><svg><use href="#i-user"/></svg>Dennis M.<span class="x">×</span></div>
              <div class="pill"><svg style="color:#8a96a6"><use href="#i-user"/></svg>Nicholas E.<span class="x">×</span></div>
              <div class="drop">Drag &amp; Drop Resources</div></div>
          </div>
          <div class="foot"><span class="who"><svg><use href="#i-user"/></svg><b>2</b></span><span class="talk"><svg><use href="#i-chat"/></svg><b>3</b></span><svg><use href="#i-chart"/></svg></div>
        </article>
        <article class="block">
          <div class="block-head"><div><h4>Oro Shipyard</h4><p>Wharf 7, Funtasea, Oroquieta City</p></div><svg><use href="#i-gear"/></svg></div>
          <div class="primary p-blue"><svg><use href="#i-tag"/></svg>Shotcrete<span class="x">×</span></div>
          <div class="split">
            <div><div class="label">PROJECT TAGS</div>
              <div class="drop">Drag &amp; Drop Tags</div></div>
            <div><div class="label">RESOURCES</div>
              <div class="pill"><svg><use href="#i-user"/></svg>Harrison J.<span class="x">×</span></div>
              <div class="drop">Drag &amp; Drop Resources</div></div>
          </div>
          <div class="foot"><span class="who"><svg><use href="#i-user"/></svg><b>1</b></span><span class="talk"><svg><use href="#i-chat"/></svg></span><svg><use href="#i-chart"/></svg></div>
        </article>
        <article class="block">
          <div class="block-head"><div><h4>ABC Oroquieta</h4><p>Poblacion 1, Town Center, Oroquieta City</p></div><svg><use href="#i-gear"/></svg></div>
          <div class="primary p-yellow"><svg><use href="#i-tag"/></svg>Steel<span class="x">×</span></div>
          <div class="split">
            <div><div class="label">PROJECT TAGS</div>
              <div class="pill"><i class="dot d-orange"></i>Barrow<span class="x">×</span></div>
              <div class="pill"><i class="dot d-red"></i>4:00 pm<span class="x">×</span></div>
              <div class="pill ok"><i class="dot d-green"></i>Confirmed<span class="x">×</span></div>
              <div class="drop">Drag &amp; Drop Tags</div></div>
            <div><div class="label">RESOURCES</div>
              <div class="pill"><svg><use href="#i-user"/></svg>Dennis M.<span class="x">×</span></div>
              <div class="pill"><svg style="color:#8a96a6"><use href="#i-user"/></svg>Nicholas E.<span class="x">×</span></div>
              <div class="drop">Drag &amp; Drop Resources</div></div>
          </div>
          <div class="foot"><span class="who"><svg><use href="#i-user"/></svg><b>2</b></span><span class="talk"><svg><use href="#i-chat"/></svg><b>3</b></span><svg><use href="#i-chart"/></svg></div>
        </article>
      </div>

      <!-- column 3 -->
      <div class="col">
        <article class="block">
          <div class="block-head"><div><h4>Adelaida Residence</h4><p>Main St., Airport Road, Caloocan</p></div><svg><use href="#i-gear"/></svg></div>
          <div class="primary p-blue"><svg><use href="#i-tag"/></svg>Shotcrete<span class="x">×</span></div>
          <div class="split">
            <div><div class="label">PROJECT TAGS</div><div class="drop">Drag &amp; Drop Tags</div></div>
            <div><div class="label">RESOURCES</div><div class="drop">Drag &amp; Drop Resources</div></div>
          </div>
          <div class="foot"><span class="who"><svg><use href="#i-user"/></svg><b>0</b></span><span class="talk"><svg><use href="#i-chat"/></svg></span><svg><use href="#i-chart"/></svg></div>
        </article>
        <article class="block">
          <div class="block-head"><div><h4>Vista Verde Village</h4><p>Pueblo Township, CDO City</p></div><svg><use href="#i-gear"/></svg></div>
          <div class="primary p-yellow"><svg><use href="#i-tag"/></svg>Steel<span class="x">×</span></div>
          <div class="split">
            <div><div class="label">PROJECT TAGS</div>
              <div class="pill"><i class="dot d-orange"></i>Barrow<span class="x">×</span></div>
              <div class="pill"><i class="dot d-red"></i>4:00 pm<span class="x">×</span></div>
              <div class="pill ok"><i class="dot d-green"></i>Confirmed<span class="x">×</span></div>
              <div class="drop">Drag &amp; Drop Tags</div></div>
            <div><div class="label">RESOURCES</div>
              <div class="pill"><svg><use href="#i-user"/></svg>Maynard L.<span class="x">×</span></div>
              <div class="pill"><svg style="color:#8a96a6"><use href="#i-user"/></svg>Charlie J.<span class="x">×</span></div>
              <div class="drop">Drag &amp; Drop Resources</div></div>
          </div>
          <div class="foot"><span class="who"><svg><use href="#i-user"/></svg><b>1</b></span><span class="talk"><svg><use href="#i-chat"/></svg></span><svg><use href="#i-chart"/></svg></div>
        </article>
        <article class="block">
          <div class="block-head"><div><h4>Primavera Condotel</h4><p>Mastersons Avenue, Carmen Upper</p></div><svg><use href="#i-gear"/></svg></div>
          <div class="primary p-green"><svg><use href="#i-tag"/></svg>Anchoring<span class="x">×</span></div>
          <div class="split">
            <div><div class="label">PROJECT TAGS</div>
              <div class="pill"><i class="dot d-orange"></i>Dril &amp; Install<span class="x">×</span></div>
              <div class="pill"><i class="dot d-purple"></i>Night Shift<span class="x">×</span></div>
              <div class="pill"><i class="dot d-red"></i>8:00 pm<span class="x">×</span></div>
              <div class="pill ok"><i class="dot d-green"></i>Confirmed<span class="x">×</span></div>
              <div class="drop">Drag &amp; Drop Tags</div></div>
            <div><div class="label">RESOURCES</div>
              <div class="pill"><svg><use href="#i-user"/></svg>Alexander G.<span class="x">×</span></div>
              <div class="pill"><svg style="color:#8a96a6"><use href="#i-user"/></svg>Joseph S.<span class="x">×</span></div>
              <div class="pill"><svg style="color:#8a96a6"><use href="#i-user"/></svg>Richard T.<span class="x">×</span></div>
              <div class="drop">Drag &amp; Drop Resources</div></div>
          </div>
          <div class="foot"><span class="who"><svg><use href="#i-user"/></svg><b>3</b></span><span class="talk"><svg><use href="#i-chat"/></svg><b>4</b></span><svg><use href="#i-chart"/></svg></div>
        </article>
      </div>

      <!-- column 4 -->
      <div class="col">
        <article class="block">
          <div class="block-head"><div><h4>Primavera Condotel</h4><p>Mastersons Avenue, Carmen Upper</p></div><svg><use href="#i-gear"/></svg></div>
          <div class="primary p-green"><svg><use href="#i-tag"/></svg>Anchoring<span class="x">×</span></div>
          <div class="split">
            <div><div class="label">PROJECT TAGS</div>
              <div class="pill"><i class="dot d-orange"></i>Dril &amp; Install<span class="x">×</span></div>
              <div class="pill"><i class="dot d-purple"></i>Night Shift<span class="x">×</span></div>
              <div class="pill"><i class="dot d-red"></i>8:00 pm<span class="x">×</span></div>
              <div class="pill ok"><i class="dot d-green"></i>Confirmed<span class="x">×</span></div>
              <div class="drop">Drag &amp; Drop Tags</div></div>
            <div><div class="label">RESOURCES</div>
              <div class="pill"><svg><use href="#i-user"/></svg>Alexander G.<span class="x">×</span></div>
              <div class="pill"><svg style="color:#8a96a6"><use href="#i-user"/></svg>Joseph S.<span class="x">×</span></div>
              <div class="pill"><svg style="color:#8a96a6"><use href="#i-user"/></svg>Richard T.<span class="x">×</span></div>
              <div class="drop">Drag &amp; Drop Resources</div></div>
          </div>
          <div class="foot"><span class="who"><svg><use href="#i-user"/></svg><b>3</b></span><span class="talk"><svg><use href="#i-chat"/></svg><b>4</b></span><svg><use href="#i-chart"/></svg></div>
        </article>
        <article class="block">
          <div class="block-head"><div><h4>Eco Park del Sol</h4><p>City Tourism Complex, Ozamiz City</p></div><svg><use href="#i-gear"/></svg></div>
          <div class="primary p-blue"><svg><use href="#i-tag"/></svg>Shotcrete<span class="x">×</span></div>
          <div class="split">
            <div><div class="label">PROJECT TAGS</div>
              <div class="pill"><i class="dot d-orange"></i>Kellmor<span class="x">×</span></div>
              <div class="pill"><i class="dot d-red"></i>7:30 am<span class="x">×</span></div>
              <div class="drop">Drag &amp; Drop Tags</div></div>
            <div><div class="label">RESOURCES</div>
              <div class="pill"><svg><use href="#i-user"/></svg>Zachary E.<span class="x">×</span></div>
              <div class="drop">Drag &amp; Drop Resources</div></div>
          </div>
          <div class="foot"><span class="who"><svg><use href="#i-user"/></svg><b>1</b></span><span class="talk"><svg><use href="#i-chat"/></svg></span><svg><use href="#i-chart"/></svg></div>
        </article>
        <article class="block">
          <div class="block-head"><div><h4>Adelaida Residence</h4><p>Main St., Airport Road, Caloocan</p></div><svg><use href="#i-gear"/></svg></div>
          <div class="primary p-blue"><svg><use href="#i-tag"/></svg>Shotcrete<span class="x">×</span></div>
          <div class="split">
            <div><div class="label">PROJECT TAGS</div><div class="drop">Drag &amp; Drop Tags</div></div>
            <div><div class="label">RESOURCES</div><div class="drop">Drag &amp; Drop Resources</div></div>
          </div>
          <div class="foot"><span class="who"><svg><use href="#i-user"/></svg><b>0</b></span><span class="talk"><svg><use href="#i-chat"/></svg></span><svg><use href="#i-chart"/></svg></div>
        </article>
      </div>
    </div>
  </main>
</div>
</body>
</html>
```